Business Card Design

This is a new business to be run from my home. I have attended certificate workshops run by Dr Kevin Ruddock who is a Master Trainer in Gentle Flow for Mobility.
I wish to communicate to people that Tai Chi is for everyone, no matter their age, gender or fitness levels. Tai Chi is taught both standing & seated.
The card should have a slightly Asian feel, mainly printed in black & white with perhaps a little soft pink &/or green.

Target Market(s)

people of all ages from 10 years up, poor fitness & mild disabilities.

Industry/Entity Type

Fitness

Contact Information for Business Card

Marrowdene Flowing Arts for Body, Mind & Stillness

Brenna Holcroft, Certificated Leader

ph 5281 9046

Requirements
Nice to have
• a feeling of health & peace.
Should not have
• bright colours, fancy fonts

```html
<!DOCTYPE html>
<html lang="en">
<head>
<meta charset="utf-8">
<title>Marrowdene Flowing Arts – Business Card</title>
<link rel="stylesheet" href="https://fonts.googleapis.com/css2?family=Itim&family=Quicksand:wght@300;400&family=Raleway:ital,wght@1,400&display=swap">
<style>
  :root {
    --page: #ffffff;
    --sky-deep: #2e3136;
    --sky-mid: #51555c;
    --sky-haze: #8d9096;
    --horizon-pink: #cfb3b3;
    --horizon-light: #e4dcd6;
    --sea-green: #6f8a84;
    --sea-soft: #92a8a1;
    --shore: #c9bfb0;
    --glow-green: rgba(170, 205, 190, 0.35);
    --ink-light: #ffffff;
    --phone-tone: #efd8c4;
    --figure-veil: rgba(255, 255, 255, 0.16);
  }

  * { margin: 0; padding: 0; box-sizing: border-box; }

  html, body {
    width: 1200px;
    height: 693px;
    overflow: hidden;
    background: var(--page);
  }

  .card {
    position: absolute;
    left: 14px;
    top: 14px;
    width: 1160px;
    height: 650px;
    overflow: hidden;
    box-shadow: 6px 8px 14px rgba(0, 0, 0, 0.45);
  }

  .card__scene {
    position: absolute;
    inset: 0;
    background:
      radial-gradient(ellipse 360px 280px at 1080px 120px, var(--glow-green), transparent 70%),
      linear-gradient(180deg,
        var(--sky-deep) 0%,
        var(--sky-mid) 30%,
        var(--sky-haze) 46%,
        var(--horizon-pink) 53%,
        var(--horizon-light) 56%,
        var(--sea-green) 60%,
        var(--sea-green) 78%,
        var(--sea-soft) 88%,
        var(--shore) 100%);
  }

  .card__figure {
    position: absolute;
    left: 50px;
    top: 160px;
    width: 300px;
    height: 390px;
    border-radius: 50%;
    background: radial-gradient(ellipse at 50% 50%, var(--figure-veil), transparent 70%);
  }

  .card__title {
    position: absolute;
    font-family: "Itim", sans-serif;
    font-weight: 400;
    color: var(--ink-light);
    text-shadow: 1px 2px 3px rgba(0, 0, 0, 0.45);
    white-space: nowrap;
    line-height: 1;
    text-align: center;
  }

  .card__title--line1 {
    top: 48px;
    left: 70px;
    width: 1010px;
    font-size: 70px;
  }

  .card__title--line2 {
    top: 160px;
    left: 375px;
    width: 670px;
    font-size: 70px;
  }

  .card__name {
    position: absolute;
    right: 34px;
    top: 522px;
    font-family: "Quicksand", sans-serif;
    font-weight: 300;
    font-size: 62px;
    line-height: 1;
    color: var(--ink-light);
    letter-spacing: 1px;
    white-space: nowrap;
  }

  .card__role {
    position: absolute;
    right: 34px;
    top: 598px;
    font-family: "Raleway", sans-serif;
    font-style: italic;
    font-size: 24px;
    line-height: 1;
    color: var(--ink-light);
  }

  .card__phone {
    position: absolute;
    left: 152px;
    top: 580px;
    font-family: "Quicksand", sans-serif;
    font-weight: 400;
    color: var(--phone-tone);
    line-height: 1;
    white-space: nowrap;
  }

  .card__phone-label { font-size: 24px; margin-right: 6px; }
  .card__phone-number { font-size: 42px; letter-spacing: 2px; }
</style>
</head>
<body>
  <div class="card">
    <div class="card__scene" role="img" aria-label="Calm muted seascape at dusk: soft grey sky with a pale moon, faint pink horizon, grey-green sea and pale shore"></div>
    <div class="card__figure" role="img" aria-label="White outline illustration of a tai chi practitioner in a low stance"></div>

    <h1 class="card__title card__title--line1">Marrowdene Flowing Arts for Body</h1>
    <p class="card__title card__title--line2">Mind &amp; Stillness</p>

    <p class="card__phone"><span class="card__phone-label">ph</span><span class="card__phone-number">5281 9046</span></p>

    <p class="card__name">Brenna Holcroft</p>
    <p class="card__role">Certificated Leader</p>
  </div>
</body>
</html>
```